Design a helpdesk ticketing platform *

We are launching a helpdesk ticketing platform. Very much like quellbox.com, merrylark.com, pivolta.com, brisktray.com etc. We have a full mid-fidelity prototype built and we want someone to build the full fidelity of the product.

You can view the full mid-fidelity prototype here: https://lnk.vexora.net/Qa8Lpw

The best way moving forward is to just design the following 4 pages

- Main Dashboard https://lnk.vexora.net/81hRtd
- All tickets https://lnk.vexora.net/jwNoEb
- Viewing a ticket https://lnk.vexora.net/Ys4VmK
- Contacts https://lnk.vexora.net/pHeXuo

Target Market(s)

Small business owners

Industry/Entity Type

Saas

Number of Pages Required

4 page

Font styles to use
Serif
Sans Serif

Colors

Designer to choose colors to be used in the design.

Requirements
Must have
• Must follow the prototype exactly. We are not looking for any UX changes. We want the designe xactly as the prototype is. We are only looking for design ideas.
Should not have
• modern, clean. We'd love to see the primary color as yellow, purple, orange, green or blue. You choose which one you think looks best and go with that.

```html
<!DOCTYPE html>
<html lang="en">
<head>
<meta charset="utf-8">
<title>Deskhaven – Dashboard</title>
<link rel="stylesheet" href="https://fonts.googleapis.com/css2?family=Nunito+Sans:wght@300;400;600;700;800&display=swap">
<style>
:root{
  --lavender:#9d84d8;
  --sidebar:#2f3140;
  --sidebar-active:#25262f;
  --sidebar-text:#b7b9c4;
  --ink:#2b2b33;
  --muted:#9a9aa3;
  --deep-purple:#55369c;
  --banner-start:#4a3288;
  --banner-end:#8d5fd8;
  --stats-bg:#ebe9ec;
  --panel-bg:#ffffff;
  --panel-head:#f0f0f4;
  --item-bg:#f8f8f8;
  --item-border:#e6e6e9;
  --stamp-bg:#ececee;
  --tag:#a88ddc;
  --tag-fold:#55369c;
  --page:#f1f1f3;
}
*{box-sizing:border-box;margin:0;padding:0}
html,body{width:1200px;height:1022px;overflow:hidden}
body{font-family:"Nunito Sans",sans-serif;background:var(--page);color:var(--ink);position:relative}

.sidebar{position:absolute;left:0;top:0;width:277px;height:1022px;background:var(--sidebar)}
.brand-area{height:146px;background:var(--lavender);position:relative}
.brand-name{position:absolute;left:54px;top:26px;color:#fff;font-size:24px;font-weight:700}
.menu-toggle{position:absolute;left:221px;top:20px}
.new-ticket{position:absolute;left:28px;top:90px;width:222px;height:47px;border-radius:24px;background:var(--deep-purple);border:1.5px solid #c9b8ef;color:#fff;font-size:19px;font-weight:700;letter-spacing:.5px;display:flex;align-items:center;padding-left:37px;gap:30px}
.nav{list-style:none;margin-top:24px}
.nav-item{height:57px;display:flex;align-items:center;padding-left:19px;color:var(--sidebar-text);font-size:15.5px;letter-spacing:.3px;position:relative}
.nav-item svg.icon{width:28px;height:28px;margin-right:22px}
.nav-item.active{background:var(--sidebar-active);color:#fff}
.nav-item .chev{position:absolute;right:18px;top:21px}

.topbar{position:absolute;left:277px;top:0;right:0;height:83px;background:#fff}
.page-title{position:absolute;left:32px;top:28px;font-size:20px}
.search{position:absolute;left:410px;top:23px;width:249px;height:37px;border:1px solid #d4d4d8;border-radius:19px;font-size:15px;color:#777;padding:9px 17px}
.search svg{position:absolute;right:13px;top:9px}
.user{position:absolute;left:695px;top:0;width:228px;height:83px;background:#f1f1f3}
.avatar{position:absolute;left:-25px;top:16px}
.user-name{position:absolute;left:36px;top:29px;font-size:19px;color:#333}
.user .chev{position:absolute;right:10px;top:36px}

.greeting{position:absolute;left:277px;top:83px;right:0;height:63px;background:linear-gradient(90deg,var(--banner-start),var(--banner-end));color:#fff;font-size:28px;font-weight:300;padding:15px 27px}
.greeting strong{font-weight:600}

.stats{position:absolute;left:277px;top:146px;right:0;height:186px;background:var(--stats-bg)}
.stat{position:absolute;top:18px;width:129px;height:152px;background:#fff;clip-path:polygon(50% 0,100% 24%,100% 76%,50% 100%,0 76%,0 24%);text-align:center;padding-top:42px}
.stat-value{font-size:36px;font-weight:700;line-height:1;color:var(--ink)}
.stat-label{font-size:15px;color:var(--muted);margin-top:6px}
.stat.primary .stat-label{color:var(--ink)}
.stat.zero .stat-value{color:#a9a9af}

.activities{position:absolute;left:305px;top:360px;width:867px;height:633px;background:var(--panel-bg);border:1px solid #e8e8eb;border-radius:4px}
.activities-head{height:46px;background:var(--panel-head);font-size:19px;padding:11px 16px}
.day-tag{position:absolute;left:-11px;height:26px;background:var(--tag);color:#fff;font-size:16px;letter-spacing:.5px;padding:3px 20px 0 25px;border-radius:13px}
.day-tag::after{content:"";position:absolute;left:0;top:13px;width:11px;height:21px;background:var(--tag-fold);border-radius:6px 0 0 6px;z-index:-1}
.activity{position:absolute;left:27px;width:813px;height:83px;background:var(--item-bg);border:1px solid var(--item-border);border-radius:3px;padding:19px 19px 0}
.stamp{display:inline-block;background:var(--stamp-bg);font-size:13px;padding:2px 8px;color:#333}
.stamp span{color:#888}
.activity p{font-size:15px;color:#3a3a40;margin-top:7px}
</style>
</head>
<body>

<aside class="sidebar">
  <div class="brand-area">
    <div class="brand-name">Deskhaven</div>
    <svg class="menu-toggle" width="40" height="44" viewBox="0 0 40 44">
      <polygon points="20,1 38,11.5 38,32.5 20,43 2,32.5 2,11.5" fill="#e9e3f6"/>
      <rect x="9" y="14" width="22" height="2.6" rx="1" fill="#2f3140"/>
      <rect x="9" y="20.7" width="22" height="2.6" rx="1" fill="#2f3140"/>
      <rect x="9" y="27.4" width="22" height="2.6" rx="1" fill="#2f3140"/>
    </svg>
    <div class="new-ticket">NEW TICKET
      <svg width="16" height="10" viewBox="0 0 16 10"><path d="M1 1l7 7 7-7" fill="none" stroke="#fff" stroke-width="2.2"/></svg>
    </div>
  </div>
  <ul class="nav">
    <li class="nav-item active">
      <svg class="icon" viewBox="0 0 28 28" fill="none" stroke="#fff" stroke-width="1.4"><circle cx="14" cy="14" r="11"/><path d="M14 14l4-6"/><path d="M7 14h2M19 14h2M14 7v2M9 9l1.4 1.4"/><path d="M8 20h12"/></svg>DASHBOARD</li>
    <li class="nav-item">
      <svg class="icon" viewBox="0 0 28 28" fill="none" stroke="#8a8c98" stroke-width="1.4"><rect x="3" y="8" width="22" height="12" rx="2"/><path d="M6 5h16M6 23h16M8 14h12"/></svg>TICKETS
      <svg class="chev" width="17" height="11" viewBox="0 0 17 11"><path d="M1 1l7.5 7.5L16 1" fill="none" stroke="#9a9ca8" stroke-width="2"/></svg></li>
    <li class="nav-item">
      <svg class="icon" viewBox="0 0 28 28" fill="none" stroke="#8a8c98" stroke-width="1.4"><rect x="2" y="6" width="24" height="16" rx="1"/><path d="M2 6l12 10 12-10M2 22l9-8M26 22l-9-8"/></svg>CONTACTS</li>
    <li class="nav-item">
      <svg class="icon" viewBox="0 0 28 28" fill="none" stroke="#8a8c98" stroke-width="1.4"><circle cx="14" cy="14" r="5"/><circle cx="14" cy="14" r="10" stroke-dasharray="4 2.3"/></svg>ADMIN SETTINGS
      <svg class="chev" width="17" height="11" viewBox="0 0 17 11"><path d="M1 1l7.5 7.5L16 1" fill="none" stroke="#9a9ca8" stroke-width="2"/></svg></li>
    <li class="nav-item">
      <svg class="icon" viewBox="0 0 28 28" fill="none" stroke="#8a8c98" stroke-width="1.4"><rect x="2" y="6" width="24" height="16" rx="2"/><path d="M2 11h24M5 17h6"/></svg>ACCOUNT &amp; BILLING</li>
  </ul>
</aside>

<header class="topbar">
  <div class="page-title">Dasboard</div>
  <div class="search">Search
    <svg width="19" height="19" viewBox="0 0 19 19"><circle cx="8" cy="8" r="6.5" fill="none" stroke="#555" stroke-width="1.8"/><path d="M13 13l5 5" stroke="#555" stroke-width="1.8"/></svg>
  </div>
  <div class="user">
    <svg class="avatar" width="48" height="52" viewBox="0 0 48 52">
      <polygon points="24,1 46,13.5 46,38.5 24,51 2,38.5 2,13.5" fill="#6a3fb6"/>
      <text x="24" y="32" text-anchor="middle" font-family="Nunito Sans, sans-serif" font-size="18" font-weight="700" fill="#fff">AK</text>
    </svg>
    <div class="user-name">Adrian Kessler</div>
    <svg class="chev" width="17" height="11" viewBox="0 0 17 11"><path d="M1 1l7.5 7.5L16 1" fill="none" stroke="#333" stroke-width="2"/></svg>
  </div>
</header>

<section class="greeting">Good Morning, <strong>Adrian</strong></section>

<section class="stats">
  <div class="stat primary" style="left:28px"><div class="stat-value">16</div><div class="stat-label">Open Tickets</div></div>
  <div class="stat" style="left:176px"><div class="stat-value">14</div><div class="stat-label">Due Today</div></div>
  <div class="stat" style="left:324px"><div class="stat-value">14</div><div class="stat-label">Unassigned</div></div>
  <div class="stat zero" style="left:471px"><div class="stat-value">0</div><div class="stat-label">Over Due</div></div>
  <div class="stat zero" style="left:619px"><div class="stat-value">0</div><div class="stat-label">On Hold</div></div>
  <div class="stat" style="left:767px"><div class="stat-value">11</div><div class="stat-label">Not Resolved</div></div>
</section>

<section class="activities">
  <div class="activities-head">Recent Activities</div>

  <div class="day-tag" style="top:67px">TODAY</div>
  <div class="activity" style="top:104px"><span class="stamp">4:49 <span>pm</span></span><p>Jerome Tay assigned forgot to cc, trying again (#15) to Jerome Tay.</p></div>
  <div class="activity" style="top:197px"><span class="stamp">10:49 <span>am</span></span><p>Jerome Tay assigned forgot to cc, trying again (#15) to Jerome Tay.</p></div>
  <div class="activity" style="top:291px"><span class="stamp">9:49 <span>am</span></span><p>Jerome Tay added a note to the ticket Test From Email (#12)</p></div>

  <div class="day-tag" style="top:393px">YESTERDAY</div>
  <div class="activity" style="top:428px"><span class="stamp">5:49 <span>pm</span></span><p>Jerome Tay assigned test (#15)</p></div>
  <div class="activity" style="top:521px"><span class="stamp">12:00 <span>pm</span></span><p>Kwan Jia Li raised a new ticket test (#16)</p></div>
</section>

</body>
</html>
```